Card Game for Leadership Development

UPDATED PROJECT, PLEASE READ!!
We have a unique tool for leaders in the workplace. It is a card deck where people draw one card that assigns a task to be completed that week. They practice developing skills that will improve their capacity for leadership.
We are going to stay with the original back of the card but still need a new front. Please see the attached back in "Leadership Back.jpg". The front needs to be 5 inches tall and 3.5 inches wide as well. Must be done in CMYK for printing. The 'Run Deep" file is how the front use to be set up but now it is needing to accommodate the description not just the title. We added an example of the text the front would need to accomodate, see TextSmile.pdf. And please see examples entitled "Tidewell" which is the example of the front of another deck... the format of the front should be the same as this deck but the design should match the leadership back. Not looking for exactly the same front as the original, please be creative and don't hesitate to ask questions.

Target Market(s)

Professionals, modern forward thinking management. Corporate People.

Other font styles liked:
• possible Sansation

Colors
3176b5
0792cd
33a6d7
85cae6
cee9f5
3276b5
85abd2
cedeed
ecf3f8

Requirements
Must have
• Must be professional, modern, sleek looking. Resemble the LeadershipBack files as far as color and design features so they go together well
Nice to have
• Insightful, thought provoking design...
Should not have
• Please nothing super complicated or busy looking or photographs.

```html
<!DOCTYPE html>
<html lang="en">
<head>
<meta charset="utf-8">
<title>Smile – Leadership Card Front</title>
<link href="https://fonts.googleapis.com/css2?family=Russo+One&family=Play:wght@400;700&display=swap" rel="stylesheet">
<style>
  :root {
    --page-bg: #e9e6e2;
    --card-deep: #1660c4;
    --card-mid: #2a7fd8;
    --card-light: #3f95e4;
    --accent-sky: #85cae6;
    --accent-pale: #cee9f5;
    --text-white: #ffffff;
  }
  html, body {
    margin: 0;
    padding: 0;
    width: 1200px;
    height: 960px;
    overflow: hidden;
    background: var(--page-bg);
  }
  .stage {
    width: 1200px;
    height: 960px;
    display: flex;
    align-items: center;
    justify-content: center;
  }
  .card-front {
    position: relative;
    width: 602px;
    height: 860px;
    background: linear-gradient(160deg, var(--card-deep) 0%, var(--card-mid) 45%, var(--card-light) 100%);
    overflow: hidden;
    box-sizing: border-box;
  }
  .card-decoration {
    position: absolute;
    left: -80px;
    bottom: -90px;
    width: 460px;
    height: 460px;
    border-radius: 50%;
    background: radial-gradient(circle, rgba(133,202,230,0.28) 0%, rgba(133,202,230,0.12) 45%, rgba(133,202,230,0) 70%);
  }
  .card-top-glow {
    position: absolute;
    left: 0;
    top: 0;
    width: 100%;
    height: 200px;
    background: linear-gradient(180deg, rgba(206,233,245,0.14), rgba(206,233,245,0));
  }
  .card-title {
    position: relative;
    margin: 36px 0 0;
    text-align: center;
    font-family: "Russo One", sans-serif;
    font-size: 80px;
    line-height: 1;
    letter-spacing: 2px;
    color: var(--text-white);
  }
  .card-task {
    position: relative;
    margin: 58px 50px 0;
    font-family: "Play", sans-serif;
    font-size: 19.5px;
    line-height: 27px;
    text-align: justify;
    color: var(--text-white);
  }
  .card-brand {
    position: absolute;
    left: 0;
    right: 0;
    bottom: 36px;
    display: flex;
    align-items: center;
    justify-content: center;
    gap: 12px;
    padding-left: 90px;
  }
  .brand-dot {
    width: 34px;
    height: 34px;
    border-radius: 50%;
    border: 2px solid var(--accent-pale);
    box-sizing: border-box;
  }
  .brand-name {
    font-family: "Play", sans-serif;
    font-size: 18px;
    color: var(--accent-pale);
    letter-spacing: 1px;
  }
</style>
</head>
<body>
<main class="stage">
  <article class="card-front">
    <div class="card-top-glow"></div>
    <div class="card-decoration" role="img" aria-label="Faint compass and gear motif in light blue tones"></div>
    <h1 class="card-title">SMILE</h1>
    <p class="card-task">There is really nothing that lights up a room, or a person’s mood more than an authentic smile. Many times leaders can get overwhelmed, preoccupied and stressed out. Employees pick up on this and will subconsciously start avoiding and reisting you or begin to reflect your negetivity. Be mindful of the energy you are sending out to other people. Appreciate the difference between passing by someone in the hall who is lost int he stress of their thoughts and worries as opposed to someone who acknowledges other people’s presence with and authentic smile. The difference is like night and day. Spend this week smiling at every chance you get. Smile when passing in hallways, while people walk in for meetings, when they come into your office. Keep in mind, an authentic smile is shown not only with your mouth but with your eyws as well. Even smiling while you talk to someone on the phone will shift your voice to a more positive tone. It’s a little thing that makes BIG difference.</p>
    <div class="card-brand">
      <span class="brand-dot"></span>
      <span class="brand-name">Keystone Lead</span>
    </div>
  </article>
</main>
</body>
</html>
```